Telmoro Business Card

I already have the conplay logo. I need to develop a professional business card layout

Target Market(s)

Business

Industry/Entity Type

Business

Contact Information for Business Card

Company Name: Telmoro Limited

Font styles to use
Sans Serif

Colors

Designer to choose colors to be used in the design.

Requirements
Must have
• Use current logo
• Need two card size options:
• Small Card: 70mm x 28mm (Landscape)
• Square Card: 65mm x 65mm
Nice to have
• I will need 8-10 files for each name, number and email address (details to follow)

```html
<!DOCTYPE html>
<html lang="en">
<head>
<meta charset="utf-8">
<title>Telmoro Business Card Template</title>
<link rel="stylesheet" href="https://fonts.googleapis.com/css2?family=Montserrat:wght@300;400;500;700;800&display=swap">
<style>
  :root {
    --dark: #1f2a2f;
    --light: #d7dcdf;
    --white: #ffffff;
    --ink: #2b2b2b;
    --green: #1a9a48;
    --lime: #9cc63b;
    --yellow: #f4b41a;
    --red: #e4322b;
    --blue: #2aa7df;
    --navy: #2e4a9b;
    --brand: #2aa7df;
  }
  * { box-sizing: border-box; margin: 0; padding: 0; }
  html, body { width: 971px; height: 1200px; overflow: hidden; }
  body { font-family: "Montserrat", sans-serif; position: relative; }

  .board { position: absolute; left: 0; width: 971px; }
  .board--dark { top: 0; height: 600px; background: var(--dark); }
  .board--light { top: 600px; height: 600px; background: var(--light); }

  .headline { position: absolute; left: 130px; top: 62px; color: var(--white); line-height: 1.05; }
  .headline__thin { display: block; font-weight: 300; font-size: 62px; letter-spacing: 1px; }
  .headline__bold { display: block; font-weight: 800; font-size: 48px; letter-spacing: 2px; margin-top: 4px; }

  .subhead { position: absolute; left: 554px; top: 160px; color: var(--white);
    font-weight: 300; font-size: 31px; line-height: 1.18; letter-spacing: .5px; }

  .card { position: absolute; background: var(--white); overflow: hidden;
    box-shadow: 6px 8px 14px rgba(0,0,0,.28); color: var(--ink); }

  .wordmark { position: absolute; font-weight: 800; color: var(--brand); letter-spacing: .5px; line-height: 1; }

  .company { position: absolute; font-weight: 400; line-height: 1; letter-spacing: .3px; }
  .fields { position: absolute; list-style: none; font-size: 9.5px; line-height: 1; }

  .dashes { position: absolute; display: flex; gap: 5px; }
  .dashes span { width: 11px; height: 2px; }

  .deco { position: absolute; font-weight: 800; color: var(--brand); line-height: 1; white-space: nowrap; }

  /* Square card 65x65 */
  .card--square { width: 287px; height: 286px; border-radius: 18px; }
  .card--square .wordmark { left: 29px; top: 31px; font-size: 29px; }
  .card--square .company { left: 29px; top: 116px; font-size: 12px; }
  .card--square .dashes { left: 29px; top: 134px; }
  .card--square .fields { left: 29px; top: 145px; }
  .card--square .fields li { height: 16.5px; }
  .card--square .deco { font-size: 60px; left: 344px; bottom: 0; transform-origin: left bottom;
    transform: rotate(-90deg); letter-spacing: -1px; }

  /* Small card 70x28 */
  .card--small { width: 309px; height: 124px; }
  .card--small .wordmark { left: 13px; top: 40px; font-size: 17px; }
  .card--small .rule { position: absolute; left: 107px; top: 0; width: 3px; height: 90px;
    display: flex; flex-direction: column; }
  .card--small .rule span { flex: 1; }
  .card--small .company { left: 149px; top: 8px; font-size: 13px; }
  .card--small .fields { left: 118px; top: 27px; font-size: 9px; }
  .card--small .fields li { height: 17.5px; }
  .card--small .deco { font-size: 56px; left: 8px; bottom: -20px; letter-spacing: 2px; }

  .c-green { background: var(--green); }
  .c-lime { background: var(--lime); }
  .c-yellow { background: var(--yellow); }
  .c-red { background: var(--red); }
  .c-blue { background: var(--blue); }
  .c-navy { background: var(--navy); }
</style>
</head>
<body>

<section class="board board--dark">
  <h1 class="headline">
    <span class="headline__thin">CREATIVE</span>
    <span class="headline__bold">MODERN</span>
  </h1>
  <p class="subhead">BUSINESS CARD<br>TEMPLATE</p>

  <article class="card card--square" style="left:129px; top:242px;">
    <div class="wordmark">TELMORO</div>
    <div class="deco" aria-hidden="true">TELMORO</div>
    <p class="company">TELMORO LIMITED</p>
    <div class="dashes"><span class="c-green"></span><span class="c-blue"></span><span class="c-yellow"></span><span class="c-red"></span><span class="c-yellow"></span><span class="c-blue"></span></div>
    <ul class="fields"><li>Name:</li><li>Address:</li><li>Mobile:</li><li>Email:</li></ul>
  </article>

  <article class="card card--small" style="left:552px; top:323px;">
    <div class="wordmark">TELMORO</div>
    <div class="rule"><span class="c-green"></span><span class="c-blue"></span><span class="c-yellow"></span><span class="c-red"></span><span class="c-yellow"></span></div>
    <p class="company">TELMORO LIMITED</p>
    <ul class="fields"><li>Name:</li><li>Address:</li><li>Mobile:</li><li>Email:</li></ul>
    <div class="deco" aria-hidden="true">TELMORO</div>
  </article>
</section>

<section class="board board--light">
  <article class="card card--square" style="left:129px; top:130px;">
    <div class="wordmark">TELMORO</div>
    <div class="deco" aria-hidden="true">TELMORO</div>
    <p class="company">TELMORO LIMITED</p>
    <div class="dashes"><span class="c-green"></span><span class="c-blue"></span><span class="c-yellow"></span><span class="c-red"></span><span class="c-yellow"></span><span class="c-blue"></span></div>
    <ul class="fields"><li>Name:</li><li>Address:</li><li>Mobile:</li><li>Email:</li></ul>
  </article>

  <article class="card card--small" style="left:552px; top:210px;">
    <div class="wordmark">TELMORO</div>
    <div class="rule"><span class="c-green"></span><span class="c-blue"></span><span class="c-yellow"></span><span class="c-red"></span><span class="c-yellow"></span></div>
    <p class="company">TELMORO LIMITED</p>
    <ul class="fields"><li>Name:</li><li>Address:</li><li>Mobile:</li><li>Email:</li></ul>
    <div class="deco" aria-hidden="true">TELMORO</div>
  </article>
</section>

</body>
</html>
```